K & D A/C Compressors' Business Card

Hello,

I need someone to create a new business card for my business. The name of my Business is: K & D A/C Compressors. I sell automotive air conditioning parts (a/c parts). I would like the business card to incorporate my logo, and to have an automotive feel to it. It is important that the business card feel like it is coming from an automotive parts business.

I already have a logo, which I will provide.

Thanks.
Updates

Project Deadline Extended Reason: I feel like extending the deadline until October 9, 2017, will allow for more time to design the business card. Thank you for your understanding. Added Monday, October 2, 2017

Target Market(s)

Consumers who need automotive a/c parts, and auto mechanics.

Industry/Entity Type

Automotive

Contact Information for Business Card

Business name: K & D A/C Compressors
Business Address: 48207 Southwest 36th Street, Palm Harbor Park, Florida 34218
Telephone: 305-472-1390
Fax: To be provided once I choose your design.
Website: www.kdcoolunits.example
Email: support@kdcoolunits.example
Names: To be provided once I choose your design.

Font styles to use
Sans Serif

Colors

Designer to choose colors to be used in the design.

Requirements
Must have
• The business card must include all of the "Business Card Details" and the logo I have uploaded.

```html
<!DOCTYPE html>
<html lang="en">
<head>
<meta charset="utf-8">
<title>K &amp; D A/C Compressors – Business Card</title>
<link rel="stylesheet" href="https://fonts.googleapis.com/css2?family=Montserrat:wght@300;400;500;800&display=swap">
<style>
  :root {
    --brand-blue: #0fa3dc;
    --brand-blue-deep: #0a8fcc;
    --ink: #2b2b2b;
    --muted: #9a9a9a;
    --name-grey: #a8a8a8;
    --paper: #ffffff;
    --backdrop: #e9ebee;
  }
  * { box-sizing: border-box; margin: 0; padding: 0; }
  html, body { width: 1200px; height: 900px; overflow: hidden; }
  body {
    background: var(--backdrop);
    font-family: "Montserrat", Arial, sans-serif;
    display: flex;
    flex-direction: column;
    align-items: center;
    justify-content: center;
    gap: 36px;
  }
  .card {
    position: relative;
    width: 700px;
    height: 400px;
    background: var(--paper);
    box-shadow: 0 10px 30px rgba(0,0,0,.12);
    overflow: hidden;
  }

  /* Brand side */
  .logo-panel {
    position: absolute;
    left: 150px;
    top: 0;
    width: 330px;
    height: 250px;
    background: linear-gradient(160deg, var(--brand-blue-deep), var(--brand-blue));
    border-radius: 0 0 44px 44px;
    display: flex;
    align-items: center;
    justify-content: center;
  }
  .brand-name {
    color: #fff;
    font-weight: 500;
    font-size: 30px;
    line-height: 1.25;
    text-align: center;
    letter-spacing: .5px;
  }
  .website {
    position: absolute;
    left: 0; right: 0;
    top: 312px;
    text-align: center;
    font-size: 17px;
    letter-spacing: 4px;
    color: #444;
    font-weight: 400;
  }

  /* Contact side */
  .brand-band {
    position: absolute;
    left: 0;
    top: 222px;
    width: 350px;
    height: 128px;
    background: linear-gradient(160deg, var(--brand-blue-deep), var(--brand-blue));
    border-radius: 0 40px 40px 0;
    display: flex;
    align-items: center;
    justify-content: center;
    padding-left: 40px;
  }
  .brand-band .brand-name { font-size: 25px; }
  .person {
    position: absolute;
    left: 290px;
    top: 78px;
  }
  .person-name {
    font-weight: 800;
    font-size: 30px;
    color: var(--name-grey);
    letter-spacing: .3px;
  }
  .person-name .surname { color: var(--brand-blue); }
  .person-title {
    font-weight: 300;
    font-size: 17px;
    color: var(--muted);
    margin-top: 2px;
  }
  .contact-list {
    position: absolute;
    left: 380px;
    top: 190px;
    list-style: none;
    font-size: 15px;
    color: var(--ink);
    line-height: 1.45;
  }
  .contact-list li {
    display: flex;
    align-items: flex-start;
    gap: 8px;
    margin-bottom: 3px;
  }
  .contact-list svg {
    width: 15px; height: 15px;
    flex: none;
    margin-top: 3px;
    fill: var(--brand-blue);
  }
</style>
</head>
<body>

  <section class="card card-brand-side" aria-label="Business card, brand side">
    <div class="logo-panel">
      <p class="brand-name">K &amp; D<br>A/C Compressors</p>
    </div>
    <p class="website">www.kdcoolunits.example</p>
  </section>

  <section class="card card-contact-side" aria-label="Business card, contact side">
    <div class="person">
      <p class="person-name">Marcus L. <span class="surname">Ortega</span></p>
      <p class="person-title">Treasurer</p>
    </div>

    <div class="brand-band">
      <p class="brand-name">K &amp; D<br>A/C Compressors</p>
    </div>

    <ul class="contact-list">
      <li>
        <svg viewBox="0 0 24 24" aria-hidden="true"><path d="M6.6 10.8a15 15 0 0 0 6.6 6.6l2.2-2.2a1 1 0 0 1 1-.25 11.4 11.4 0 0 0 3.6.57 1 1 0 0 1 1 1V20a1 1 0 0 1-1 1A17 17 0 0 1 3 4a1 1 0 0 1 1-1h3.5a1 1 0 0 1 1 1c0 1.25.2 2.45.57 3.57a1 1 0 0 1-.25 1z"/></svg>
        <span>305-472-1390</span>
      </li>
      <li>
        <svg viewBox="0 0 24 24" aria-hidden="true"><path d="M7 2h10v6H7zM3 9h18v12H3zm4 3v2h2v-2zm4 0v2h2v-2zm4 0v2h2v-2zm-8 4v2h2v-2zm4 0v2h2v-2zm4 0v2h2v-2z"/></svg>
        <span>(866) 730-4215</span>
      </li>
      <li>
        <svg viewBox="0 0 24 24" aria-hidden="true"><path d="M2 5h20v14H2zm2 2v.5l8 5 8-5V7l-8 5z"/></svg>
        <span>support@kdcoolunits.example</span>
      </li>
      <li>
        <svg viewBox="0 0 24 24" aria-hidden="true"><path d="M12 2a7 7 0 0 0-7 7c0 5 7 13 7 13s7-8 7-13a7 7 0 0 0-7-7zm0 9.5A2.5 2.5 0 1 1 12 6.5a2.5 2.5 0 0 1 0 5z"/></svg>
        <span>48207 Southwest 36th Street,<br>Palm Harbor Park, Florida 34218</span>
      </li>
    </ul>
  </section>

</body>
</html>
```